Website Design for Chef Varo Chinese Restaurant

Chef Varo is a new Chinese Restaurant. It offers exceptional dining experience with authentic and dynamic dishes created with quality ingredients.

A vivid website theme is required to promote this new restaurant online. Logo, menu, wine list and a few other files are attached for help with designing.

A very rough demo website has been setup and can be accessed via http://www.chefvaro.com.au. It is for telling designers what content is shown up on each page (except for homepage). By reading the about us page, designers can get some more info of Chef Varo. However, the layout, theme color, font, etc are not set in stone. Visitors should be able to feel Chef Varo restaurant's authentic Chinese cuisine and high hygiene standard. Home page of the website could be The "Our website is coming soon" description is shown on demo site but do not required to be presented on new design.

Some main pages design should be included: Home (landing page), About us, Menu (Dishes), Winelist, Gallery, Contact us. No HTML and coding required. The output should be well layered psd or png files with acceptable resolution for web use.

A few other website can be referred to are:

http://belmiraeatery.com.au/
http://www.stone-kettle.com/
http://quillhaven.com.au/
http://meadowbistro.com.au/
http://www.lanternvaledining.com.au/
http://www.thetrove.com.au/

Industry/Entity Type

Restaurant

Requirements
Nice to have
• I expect designs of at least these webpages: homepage, menu page and contact us page. If you can provide "about us" page as well, it will probably help you win the competition. well layered psd or png file is my preference.
Should not have
• You don't have to make html/cs/js or any coding. All I need is just art design

```html
<!DOCTYPE html>
<html lang="en">
<head>
<meta charset="utf-8">
<title>Chef Varo Chinese Restaurant</title>
<link rel="stylesheet" href="https://fonts.googleapis.com/css2?family=Ubuntu:wght@400;500&family=Open+Sans:wght@400;600&display=swap">
<style>
:root{
  --cream:#fffbc8;
  --red:#e5312b;
  --rust:#cd4631;
  --band:#c94b3c;
  --dark:#2b2b2b;
  --ink:#333;
  --grey:#8a8a8a;
  --rule:#e2e2e2;
  --white:#fff;
}
*{margin:0;padding:0;box-sizing:border-box}
html,body{width:1145px;height:1200px;overflow:hidden}
body{position:relative;background:var(--dark);font-family:'Ubuntu',sans-serif;color:var(--ink)}
.site-header{position:absolute;left:0;top:0;width:1145px;height:190px;background:var(--cream);border-bottom:5px solid var(--band)}
.brand{position:absolute;left:103px;top:60px;display:flex;align-items:center;gap:10px}
.brand-mark{width:14px;height:14px;background:var(--red)}
.brand-name{font-family:'Ubuntu',sans-serif;font-weight:500;font-size:17px;color:#111}
.phone{position:absolute;left:812px;top:41px;display:flex;align-items:center;gap:5px;color:var(--red);font-family:'Open Sans',sans-serif;font-size:20px}
.flags{position:absolute;left:986px;top:44px;display:flex;gap:16px}
.flags svg{display:block;border:1px solid #ccc}
.main-nav{position:absolute;right:92px;top:117px;display:flex;gap:36px;font-size:15px}
.main-nav a{color:#555;text-decoration:none}
.main-nav a.active{color:var(--red)}
.page{position:absolute;left:95px;top:190px;width:960px;height:887px;background:var(--white)}
.slider{position:absolute;left:10px;top:10px;width:940px;height:357px;background:linear-gradient(90deg,#d9c09b 0%,#e8d7bd 22%,#e86a45 40%,#d8442b 62%,#f0a98f 100%)}
.slider-arrow{position:absolute;top:154px;width:39px;height:50px;background:rgba(120,120,120,.55)}
.slider-arrow.prev{left:0}.slider-arrow.next{right:0}
.caption{position:absolute;right:0;top:250px;width:363px;height:54px;background:rgba(40,30,25,.75);color:#fff;font-family:'Open Sans',sans-serif;font-size:24px;line-height:52px;padding-left:17px}
.intro{position:absolute;left:12px;top:387px;width:690px}
.intro h1{font-weight:400;font-size:26px;color:var(--red);margin-bottom:14px}
.intro p{font-family:'Open Sans',sans-serif;font-size:14px;line-height:22px;color:var(--grey)}
.divider{position:absolute;left:10px;top:549px;width:700px;height:1px;background:var(--rule)}
.features{position:absolute;left:12px;top:588px;display:flex;gap:19px}
.feature{width:219px}
.feature h2{font-weight:400;font-size:20px;color:var(--red);margin-bottom:18px}
.feature .thumb{width:219px;height:140px}
.feature p{font-family:'Open Sans',sans-serif;font-size:11.5px;line-height:18px;color:var(--grey);margin-top:11px;padding-left:2px}
.sidebar{position:absolute;left:730px;top:391px;width:220px;height:465px;border-left:1px solid var(--rule)}
.side-title{height:44px;background:var(--rust);color:#fff;font-size:19px;line-height:44px;padding-left:20px}
.side-body{padding:12px 22px 22px;font-family:'Open Sans',sans-serif;font-size:14px;line-height:22px;color:#444}
.hours{padding-top:22px}
.hours .label{color:var(--red)}
.hours .time{color:var(--grey)}
.hours .gap{margin-top:22px}
.site-footer{position:absolute;left:96px;top:1112px;font-family:'Open Sans',sans-serif;font-size:13px;color:#ddd}
.foot-nav{display:flex;gap:12px}
.foot-nav a{color:#ddd;text-decoration:none}
.foot-nav span{color:#aaa}
.copyright{margin-top:17px}
.social{position:absolute;left:943px;top:1125px;display:flex;gap:8px}
.social span{width:32px;height:32px;border-radius:50%;display:flex;align-items:center;justify-content:center}
</style>
</head>
<body>
<header class="site-header">
  <div class="brand"><span class="brand-mark"></span><span class="brand-name">Chef Varo Chinese Restaurant</span></div>
  <div class="phone">
    <svg width="12" height="16" viewBox="0 0 12 16"><path d="M3 1 L5 4 L3.5 6 Q5 10 8 12 L10 10.5 L12 13 L9.5 15.5 Q2 12 0.5 3 Z" fill="currentColor"/></svg>
    08 7420 5563
  </div>
  <div class="flags">
    <svg width="24" height="16" viewBox="0 0 24 16" aria-label="English"><rect width="24" height="16" fill="#1f3a8a"/><path d="M0 0L24 16M24 0L0 16" stroke="#fff" stroke-width="3"/><path d="M0 0L24 16M24 0L0 16" stroke="#c8102e" stroke-width="1"/><path d="M12 0V16M0 8H24" stroke="#fff" stroke-width="5"/><path d="M12 0V16M0 8H24" stroke="#c8102e" stroke-width="3"/></svg>
    <svg width="24" height="16" viewBox="0 0 24 16" aria-label="Japanese"><rect width="24" height="16" fill="#fff"/><circle cx="12" cy="8" r="4.5" fill="#d0021b"/></svg>
  </div>
  <nav class="main-nav">
    <a class="active" href="#">Home</a><a href="#">About Us</a><a href="#">Menu</a><a href="#">Wine List</a><a href="#">Gallery</a><a href="#">Contact Us</a><a href="#">Belmira Court</a>
  </nav>
</header>

<main class="page">
  <div class="slider" role="img" aria-label="Steamed dumplings in a bamboo basket beside a whole red crab">
    <span class="slider-arrow prev"><svg width="39" height="50"><path d="M24 13 L14 25 L24 37" stroke="#fff" fill="none" stroke-width="1.5"/></svg></span>
    <span class="slider-arrow next"><svg width="39" height="50"><path d="M15 13 L25 25 L15 37" stroke="#fff" fill="none" stroke-width="1.5"/></svg></span>
    <div class="caption">Aenean tempus consequat...</div>
  </div>

  <section class="intro">
    <h1>Welcome to Chef Varo</h1>
    <p>Chef Varo is named after its’ executive chef, Mr. Varo. Chef Varo has been in his career for nearly two decades before he moved to Australia nine years ago. He settled in Adelaide then started his first restaurant, Belmira Court in Norwood. Belmira Court has been running successfully for years due to Chef Varo’s talent of cooking.</p>
  </section>
  <div class="divider"></div>

  <section class="features">
    <article class="feature">
      <h2>Our Menu</h2>
      <div class="thumb" role="img" aria-label="Salmon sashimi with garnish" style="background:linear-gradient(135deg,#f2f2ee,#f06a4a 45%,#e8553a 70%,#6b8a3a)"></div>
      <p>Donec faucibus nec enim a vehicula. Praesent auctor vel risus id porttitor. Praesent quam purus.</p>
    </article>
    <article class="feature">
      <h2>Wine List</h2>
      <div class="thumb" role="img" aria-label="Wine bottles and filled glasses" style="background:linear-gradient(90deg,#2a1a10,#7a4a22 40%,#c9a35a 60%,#5a1a14)"></div>
      <p>Donec faucibus nec enim a vehicula. Praesent auctor vel risus id porttitor. Praesent quam purus.</p>
    </article>
    <article class="feature">
      <h2>Gallery</h2>
      <div class="thumb" role="img" aria-label="Dumplings in a bamboo steamer on a mat" style="background:radial-gradient(circle at 50% 45%,#f0d9b5 0,#d9b07a 35%,#ece3d6 70%)"></div>
      <p>Donec faucibus nec enim a vehicula. Praesent auctor vel risus id porttitor. Praesent quam purus.</p>
    </article>
  </section>

  <aside class="sidebar">
    <div class="side-title">Location</div>
    <div class="side-body">12/48 Larkfield Road<br>St Peters, SA, 5069</div>
    <div class="side-title">Trading Hours</div>
    <div class="side-body hours">
      <div>We are open 7 days</div>
      <div class="gap label">Lunch</div>
      <div>Monday to Friday</div>
      <div class="time">11:30am - 2:30pm</div>
      <div class="gap">Saturday to Sunday</div>
      <div class="time">11:00am - 3:00pm</div>
      <div class="gap label">Dinner</div>
      <div>Monday to Sunday</div>
      <div class="time">6:00pm Until Late</div>
    </div>
  </aside>
</main>

<footer class="site-footer">
  <nav class="foot-nav">
    <a href="#">Home</a><span>|</span><a href="#">About Us</a><span>|</span><a href="#">Menu</a><span>|</span><a href="#">Wine List</a><span>|</span><a href="#">Gallery</a><span>|</span><a href="#">Contact Us</a><span>|</span><a href="#">Belmira Court</a>
  </nav>
  <p class="copyright">Copyright &nbsp;© &nbsp;2014 &nbsp; Chef Varo Chinese Restaurant. &nbsp; All rights reserved.</p>
</footer>
<div class="social">
  <span style="background:#3b5998" aria-label="Social link"></span>
  <span style="background:#2aa3e0" aria-label="Social link"></span>
  <span style="background:#6aa63a" aria-label="Email"><svg width="18" height="12" viewBox="0 0 18 12"><rect width="18" height="12" rx="2" fill="#fff"/><path d="M1 1 L9 7 L17 1" stroke="#6aa63a" fill="none" stroke-width="1.5"/></svg></span>
</div>
</body>
</html>
```